Flyer design for the Harvest Lantern Summit 2019 (HALSUM)

Design a flyer for our annual conference with basic information about the conference: conference logo and year, Conference name: Harvest Lantern Summit Location: Talbot Community Center (Downtown Portland)482 Wexley Street, Portland, ME 04109, Date: August 8th, 9th, 10th and 11th, 2019Start time 7:00PMI would like the following three words added to the flyer. These words describe the vision of the conference: Prophetic, Fire, Overflow,

Contact info:
Website: www.vostel.org
Phone: 207 555 3184
Email: contact@meadowcrest.org

Target Market(s)

Young adults living in the United States

Industry/Entity Type

Religious

Font styles to use
Sans Serif

Colors

Designer to choose colors to be used in the design.

Requirements
Must have
• HALSUM must logo standout, the reader should be able to take a quick look and find key info,
Should not have
• Cross image, church image

```html
<!DOCTYPE html>
<html lang="en">
<head>
<meta charset="utf-8">
<title>Harvest Lantern Summit 2019</title>
<link href="https://fonts.googleapis.com/css2?family=Urbanist:wght@400;600;700;800&display=swap" rel="stylesheet">
<style>
  :root {
    --sky-light: #5fd6fb;
    --sky-mid: #3aa6f0;
    --sky-deep: #1a4ff0;
    --cloud: #f4f6f7;
    --cloud-shade: #e4e8ea;
    --mist: #eafcfc;
    --orange: #f58a1f;
    --brand-blue: #2f7ee3;
    --white: #ffffff;
  }
  * { margin: 0; padding: 0; box-sizing: border-box; }
  html, body { width: 850px; height: 1200px; overflow: hidden; }
  body { font-family: "Urbanist", sans-serif; background: var(--white); }

  .flyer {
    position: relative;
    width: 850px;
    height: 1200px;
    overflow: hidden;
    background:
      radial-gradient(circle at 280px 260px, rgba(120,230,255,0.9) 0, rgba(90,200,250,0.5) 260px, rgba(0,0,0,0) 560px),
      linear-gradient(110deg, var(--sky-light) 0%, var(--sky-mid) 50%, var(--sky-deep) 100%);
  }

  .event-title {
    position: absolute; top: 52px; left: 0; width: 100%;
    text-align: center; color: var(--white);
    font-size: 52px; font-weight: 700; letter-spacing: 1px; line-height: 1;
  }
  .event-dates {
    position: absolute; top: 106px; left: 0; width: 100%;
    text-align: center; color: var(--white);
    font-size: 34px; font-weight: 700; line-height: 1;
  }

  .cloud-bank {
    position: absolute; left: 0; top: 690px; width: 850px; height: 441px;
    background:
      linear-gradient(180deg, rgba(234,252,252,0) 0%, rgba(234,252,252,0.75) 22%, rgba(240,252,250,0.95) 45%, #f3fcf4 100%);
  }

  .vision-cloud {
    position: absolute;
    background: var(--cloud);
    border-radius: 999px;
    box-shadow: inset 0 -10px 0 var(--cloud-shade);
    display: flex; align-items: center; justify-content: center;
    color: var(--orange); font-size: 35px; font-weight: 400;
  }
  .vision-cloud--prophetic { left: 157px; top: 160px; width: 250px; height: 125px; }
  .vision-cloud--overflow  { left: 362px; top: 305px; width: 250px; height: 140px; }
  .vision-cloud--fire      { left: -60px; top: 468px; width: 250px; height: 130px; padding-left: 60px; }

  .rocket-art {
    position: absolute; left: 185px; top: 254px; width: 192px; height: 593px;
    border-radius: 96px 96px 60px 60px;
    background: linear-gradient(180deg, rgba(230,235,240,0.55) 0%, rgba(255,210,170,0.45) 70%, rgba(255,220,180,0) 100%);
  }

  .venue {
    position: absolute; left: 517px; top: 494px; color: var(--white);
    font-size: 22px; line-height: 25.5px;
  }
  .venue-icon { display: block; margin: 0 0 14px 0; }
  .venue-name { font-weight: 700; }
  .start-time {
    position: absolute; left: 517px; top: 682px; color: var(--white);
    font-size: 22px; line-height: 1;
  }
  .start-time .clock-icon { display: block; margin-bottom: 18px; }
  .start-time strong { font-weight: 700; }

  .summit-mark {
    position: absolute; left: 0; top: 908px; width: 100%;
    text-align: center; color: var(--brand-blue);
    font-size: 148px; font-weight: 800; line-height: 1; letter-spacing: 8px;
  }
  .summit-year {
    position: absolute; left: 0; top: 1048px; width: 100%;
    display: flex; align-items: center; justify-content: center; gap: 18px;
    color: var(--orange); font-size: 60px; font-weight: 800; line-height: 1;
  }
  .summit-year-digits { letter-spacing: 42px; margin-right: -42px; }
  .summit-year-rule { width: 166px; height: 4px; background: var(--orange); }

  .contact-bar {
    position: absolute; left: 0; top: 1131px; width: 850px; height: 69px;
    background: var(--orange); color: var(--white);
    display: flex; align-items: center; justify-content: center; gap: 34px;
    font-size: 22px;
  }
  .contact-item { display: flex; align-items: center; gap: 9px; }
</style>
</head>
<body>
<main class="flyer">
  <h1 class="event-title">HARVEST LANTERN SUMMIT</h1>
  <p class="event-dates">August 8th, 9th, 10th and 11th, 2019</p>

  <div class="cloud-bank" role="img" aria-label="Soft white clouds along the lower part of the sky"></div>

  <div class="vision-cloud vision-cloud--prophetic">Prophetic</div>
  <div class="vision-cloud vision-cloud--overflow">Overflow</div>
  <div class="vision-cloud vision-cloud--fire">Fire</div>

  <div class="rocket-art" role="img" aria-label="Illustration of a rocket launching upward with flame trails"></div>

  <div class="venue">
    <svg class="venue-icon" width="34" height="46" viewBox="0 0 34 46" aria-hidden="true">
      <path d="M17 0C7.6 0 0 7.4 0 16.6 0 29 17 46 17 46s17-17 17-29.4C34 7.4 26.4 0 17 0zm0 23a7 7 0 1 1 0-14 7 7 0 0 1 0 14z" fill="var(--white)"/>
    </svg>
    <div class="venue-name">Talbot Community Center</div>
    <div>(Downtown Portland)</div>
    <div>482 Wexley Street,</div>
    <div>Portland, ME 04109</div>
  </div>

  <div class="start-time">
    <svg class="clock-icon" width="38" height="38" viewBox="0 0 38 38" aria-hidden="true">
      <circle cx="19" cy="19" r="16" fill="none" stroke="var(--white)" stroke-width="4"/>
      <path d="M19 10v10h8" fill="none" stroke="var(--white)" stroke-width="4" stroke-linecap="round"/>
    </svg>
    Start time <strong>7:00 PM</strong>
  </div>

  <div class="summit-mark">HALSUM</div>
  <div class="summit-year">
    <span class="summit-year-rule"></span>
    <span class="summit-year-digits">2019</span>
    <span class="summit-year-rule"></span>
  </div>

  <footer class="contact-bar">
    <span class="contact-item">
      <svg width="20" height="26" viewBox="0 0 20 26" aria-hidden="true"><path d="M4 1l4 1 1 6-3 2c1 4 3 7 6 9l2-3 6 1 0 4-3 4C8 25 1 15 1 5z" fill="var(--white)"/></svg>
      207 555 3184
    </span>
    <span class="contact-item">
      <svg width="30" height="22" viewBox="0 0 30 22" aria-hidden="true"><rect x="1.5" y="1.5" width="27" height="19" fill="none" stroke="var(--white)" stroke-width="2"/><path d="M2 2l13 11L28 2M2 20l9-8M28 20l-9-8" fill="none" stroke="var(--white)" stroke-width="2"/></svg>
      contact@meadowcrest.org
    </span>
    <span class="contact-item">
      <svg width="26" height="26" viewBox="0 0 26 26" aria-hidden="true"><circle cx="13" cy="13" r="11.5" fill="none" stroke="var(--white)" stroke-width="1.8"/><ellipse cx="13" cy="13" rx="5" ry="11.5" fill="none" stroke="var(--white)" stroke-width="1.5"/><path d="M1.5 13h23M3.5 7h19M3.5 19h19" stroke="var(--white)" stroke-width="1.5"/></svg>
      www.vostel.org
    </span>
  </footer>
</main>
</body>
</html>
```